Business Card Design for CoreLeafHarmony

We need the new logo on a business card for 3 employees:
Norma Kepple, PhD, Advanced Instructor and Practitioner of PulseWeave Vitalis Practice (email: norma@coreleafharmony.example)
Ted Halloran, Business Manager (email: ted@coreleafharmony.example)
Rosa Pilgrew, Administrative Assistant (email: rosa@quillgrove.example)

Target Market(s)

healthcare professionals

Industry/Entity Type

Alternative Medicine

Contact Information for Business Card

Names, titles, emails (names, titles, emails are in project description), phone, address, website, with logo and tagline. See below for address, phone, website: 418 Fennick St, Bldg 12, Ste 307
Santa Cruz, CA 95060
831-555-0174
www.coreleafharmony.example
Tagline: Craft of Balance, Light of Renewal

Font styles to use
Other font styles liked:
• Gabriela

Colors
00a990
86cfc6
6b449b
b7a5cd
85abd2
abd036

Requirements
Must have
• Colors and style that match the logo design - shades such as blue, green, purple
• Compatible or same font as in the logo
Nice to have
• Nice if it goes with the theme of Norma's last business card - uploaded below
Should not have
• colors or style in conflict with the logo

```html
<!DOCTYPE html>
<html lang="en">
<head>
<meta charset="utf-8">
<title>CoreLeafHarmony Business Card</title>
<link href="https://fonts.googleapis.com/css2?family=Gabriela&display=swap" rel="stylesheet">
<style>
  :root {
    --backdrop: #dcdcdc;
    --teal: #00a990;
    --teal-deep: #079e8a;
    --teal-soft: #2bb39f;
    --paper: #e9e9e9;
    --ink-purple: #2b1d5c;
    --white: #ffffff;
  }
  html, body {
    margin: 0;
    padding: 0;
    width: 1200px;
    height: 1200px;
    overflow: hidden;
    background: var(--backdrop);
    font-family: "Gabriela", serif;
  }
  .stage { position: relative; width: 1200px; height: 1200px; }
  .card {
    position: absolute;
    top: 454px;
    width: 514px;
    height: 293px;
    overflow: hidden;
  }
  /* Front */
  .card-front { left: 47px; background: var(--teal); }
  .front-texture {
    position: absolute; inset: 0;
    background: linear-gradient(135deg, var(--teal-soft) 0%, var(--teal) 45%, var(--teal-deep) 100%);
  }
  .front-brand {
    position: absolute;
    left: 127px; top: 88px;
    display: flex; align-items: center; gap: 14px;
  }
  .brand-dot {
    width: 96px; height: 96px; border-radius: 50%;
    background: var(--white);
  }
  .front-wordmark {
    color: var(--white);
    font-size: 30px;
    letter-spacing: 0.5px;
  }
  .front-tagline {
    position: absolute;
    left: 0; right: 0; top: 194px;
    text-align: center;
    color: var(--white);
    font-size: 11px;
    letter-spacing: 3.2px;
    text-transform: uppercase;
  }
  /* Back */
  .card-back { left: 643px; background: var(--paper); }
  .back-brand {
    position: absolute;
    left: 30px; top: 30px;
    display: flex; align-items: center; gap: 8px;
  }
  .back-brand .brand-dot {
    width: 72px; height: 72px;
    background: var(--teal);
  }
  .back-wordmark {
    color: var(--ink-purple);
    font-size: 24px;
  }
  .person {
    position: absolute;
    right: 29px; top: 116px;
    text-align: right;
  }
  .person-name {
    color: var(--ink-purple);
    font-size: 18px;
    letter-spacing: 0.5px;
    text-transform: uppercase;
    margin: 0 0 3px;
    -webkit-text-stroke: 0.4px var(--ink-purple);
  }
  .person-title {
    color: var(--teal);
    font-size: 9.5px;
    line-height: 11.5px;
    text-transform: uppercase;
    margin: 0;
  }
  .rule {
    position: absolute;
    left: 21px; right: 21px; top: 171px;
    height: 1.5px;
    background: var(--ink-purple);
  }
  .contacts {
    position: absolute;
    top: 182px; left: 27px; right: 33px;
    display: flex; justify-content: space-between;
  }
  .contact-col { display: flex; flex-direction: column; gap: 5px; }
  .contact-item {
    display: flex; align-items: center; gap: 6px;
    color: var(--teal);
    font-size: 9.8px;
    line-height: 12px;
  }
  .contact-item svg { width: 11px; height: 11px; flex: none; }
  .back-band {
    position: absolute;
    left: 0; right: 0; bottom: 0;
    height: 30px;
    background: var(--teal);
    color: var(--white);
    display: flex; align-items: center; justify-content: center;
    font-size: 11px;
    letter-spacing: 5.2px;
    text-transform: uppercase;
  }
</style>
</head>
<body>
<main class="stage">
  <section class="card card-front">
    <div class="front-texture" role="img" aria-label="Soft teal photo of DNA double helix strands"></div>
    <div class="front-brand">
      <span class="brand-dot"></span>
      <span class="front-wordmark">CoreLeafHarmony</span>
    </div>
    <p class="front-tagline">Craft of Balance, Light of Renewal</p>
  </section>

  <section class="card card-back">
    <div class="back-brand">
      <span class="brand-dot"></span>
      <span class="back-wordmark">CoreLeafHarmony</span>
    </div>
    <div class="person">
      <p class="person-name">Norma Kepple</p>
      <p class="person-title">PhD, Advanced Instructor and Practitioner<br>of PulseWeave Vitalis Practice</p>
    </div>
    <div class="rule"></div>
    <div class="contacts">
      <div class="contact-col">
        <div class="contact-item">
          <svg viewBox="0 0 12 12"><path d="M6 0.5a3.8 3.8 0 0 0-3.8 3.8C2.2 7.2 6 11.5 6 11.5s3.8-4.3 3.8-7.2A3.8 3.8 0 0 0 6 0.5zm0 5.3a1.5 1.5 0 1 1 0-3 1.5 1.5 0 0 1 0 3z" fill="#2b1d5c"/></svg>
          <span>418 Fennick St, Bldg 12, Ste 307 Santa Cruz, CA 95060</span>
        </div>
        <div class="contact-item">
          <svg viewBox="0 0 12 12"><path d="M2.6 0.8l1.8 0.2 0.9 2.6-1.2 1a7 7 0 0 0 3.3 3.3l1-1.2 2.6 0.9 0.2 1.8-1.4 1.3C5.4 10.7 1.3 6.6 1.3 2.2z" fill="#2b1d5c"/></svg>
          <span>831-555-0174</span>
        </div>
      </div>
      <div class="contact-col">
        <div class="contact-item">
          <svg viewBox="0 0 12 12"><rect x="0.8" y="2.2" width="10.4" height="7.6" fill="none" stroke="#2b1d5c" stroke-width="1"/><path d="M0.8 2.2L6 6.6l5.2-4.4" fill="none" stroke="#2b1d5c" stroke-width="1"/></svg>
          <span>norma@coreleafharmony.example</span>
        </div>
        <div class="contact-item">
          <svg viewBox="0 0 12 12" fill="none" stroke="#2b1d5c" stroke-width="0.9"><circle cx="6" cy="6" r="5.2"/><ellipse cx="6" cy="6" rx="2.3" ry="5.2"/><path d="M0.8 6h10.4M1.6 3.4h8.8M1.6 8.6h8.8"/></svg>
          <span>www.coreleafharmony.example</span>
        </div>
      </div>
    </div>
    <div class="back-band">Craft of Balance, Light of Renewal</div>
  </section>
</main>
</body>
</html>
```